Business Cards and Letterhead for Solo Attorney
Mark Whitfield, Esq., APC
Business Cards and Letterhead for Solo Attorney - Law
Creative Brief
Professional
SEE ADDITIONAL COMMENTS BELOW
742 S. Milbrook Avenue West Covina, CA 91790
mark@whitfieldlegal.example
NAME/TITLE SHOULD APPEAR AS FOLLOWS: Mark Whitfield Attorney at Law/Abogado Workers' Compensation Judge (Ret.) It should also have my corporate name somewhere: Mark Whitfield, Esq., APC

```html
<!DOCTYPE html>
<html lang="en">
<head>
<meta charset="utf-8">
<title>Mark Whitfield, Esq., APC — Business Card</title>
<link href="https://fonts.googleapis.com/css2?family=Source+Sans+3:wght@400;600;700&display=swap" rel="stylesheet">
<style>
  :root {
    --navy: #1a2f86;
    --navy-deep: #14246b;
    --gold: #b8975a;
    --gold-light: #d9c08a;
    --ink: #4a4a4a;
    --paper: #ffffff;
    --backdrop: #3a3a3a;
  }
  * { margin: 0; padding: 0; box-sizing: border-box; }
  html, body {
    width: 1200px; height: 780px; overflow: hidden;
    background: var(--backdrop);
    font-family: "Source Sans 3", sans-serif;
  }
  .business-card {
    position: absolute; left: 75px; top: 90px;
    width: 1050px; height: 600px;
    background: var(--paper);
    border-radius: 26px;
    overflow: hidden;
  }
  .card-swoosh { position: absolute; inset: 0; width: 100%; height: 100%; }
  .brand {
    position: absolute; left: 70px; top: 60px;
    display: flex; align-items: center; gap: 16px;
  }
  .brand-mark {
    width: 58px; height: 58px; background: var(--navy);
  }
  .brand-name {
    color: var(--navy); font-weight: 700; font-size: 30px;
    letter-spacing: 0.5px; text-transform: uppercase;
  }
  .attorney {
    position: absolute; right: 330px; top: 255px; text-align: right;
  }
  .attorney-name {
    color: var(--navy); font-weight: 600; font-size: 38px; line-height: 1.1;
  }
  .attorney-title {
    color: var(--gold); font-size: 23px; line-height: 1.35; margin-top: 4px;
  }
  .address {
    position: absolute; left: 70px; top: 335px;
    color: var(--ink); font-size: 21px; line-height: 1.35;
  }
  .contact-list {
    position: absolute; left: 70px; top: 420px; list-style: none;
    color: var(--ink); font-size: 21px; line-height: 1;
  }
  .contact-item { display: flex; align-items: center; gap: 14px; height: 33px; }
  .contact-icon { width: 20px; height: 20px; fill: var(--navy); flex: none; }
</style>
</head>
<body>
  <div class="business-card">
    <svg class="card-swoosh" viewBox="0 0 1050 600" preserveAspectRatio="none" aria-hidden="true">
      <defs>
        <linearGradient id="goldSheen" x1="0" y1="1" x2="1" y2="0">
          <stop offset="0" stop-color="#e6d3a6"/>
          <stop offset="0.5" stop-color="#b8975a"/>
          <stop offset="1" stop-color="#8f713d"/>
        </linearGradient>
      </defs>
      <path d="M780 0 C990 80 1030 330 960 470 C900 560 760 600 560 600 L1050 600 L1050 0 Z" fill="url(#goldSheen)"/>
      <path d="M780 0 C1000 70 1060 330 1012 462 C985 540 940 580 890 600 L1050 600 L1050 0 Z" fill="var(--navy)"/>
    </svg>

    <div class="brand">
      <div class="brand-mark"></div>
      <div class="brand-name">Mark Whitfield Esq., APC</div>
    </div>

    <div class="attorney">
      <div class="attorney-name">Mark Whitfield</div>
      <div class="attorney-title">Attorney at Law/Abogado</div>
      <div class="attorney-title">Workers' Compensation Judge (Ret.)</div>
    </div>

    <div class="address">
      742 S. Milbrook Avenue<br>
      West Covina, CA 91790
    </div>

    <ul class="contact-list">
      <li class="contact-item">
        <svg class="contact-icon" viewBox="0 0 24 24"><path d="M6.6 10.8a15 15 0 0 0 6.6 6.6l2.2-2.2c.3-.3.7-.4 1-.2 1.1.4 2.3.6 3.6.6.6 0 1 .4 1 1V20c0 .6-.4 1-1 1A17 17 0 0 1 3 4c0-.6.4-1 1-1h3.5c.6 0 1 .4 1 1 0 1.3.2 2.5.6 3.6.1.3 0 .7-.2 1z"/></svg>
        (213) 555-0184
      </li>
      <li class="contact-item">
        <svg class="contact-icon" viewBox="0 0 24 24"><path d="M6 2h12v6H6z"/><path d="M3 9h18v9h-3v4H6v-4H3zm5 6v5h8v-5z"/></svg>
        (213) 555-0127
      </li>
      <li class="contact-item">
        <svg class="contact-icon" viewBox="0 0 24 24"><path d="M2 5h20v14H2z"/><path d="M2 5l10 8 10-8" fill="none" stroke="#fff" stroke-width="2"/></svg>
        mark@whitfieldlegal.example
      </li>
      <li class="contact-item">
        <svg class="contact-icon" viewBox="0 0 24 24"><circle cx="12" cy="12" r="10"/><path d="M2 12h20M12 2c3 3 3 17 0 20M12 2c-3 3-3 17 0 20" fill="none" stroke="#fff" stroke-width="1.5"/></svg>
        www.whitfieldlegal.example
      </li>
    </ul>
  </div>
</body>
</html>
```